Restaurant Poster Design Project for A-Frame

I am after a poster, which will go on an outdoor A-Frame (A1 size - this size is to be confirmed) outlining our drink/happy hour/specials for our Mexican Restaurant and Bar.

Specific details are:

$4 Beer, Wine and Spirits
$5 Margaritas
everynight 5:30pm-7:30pm

I will supply logo, which needs to be incorporated (really small) into the poster, along with our address: 42 Lowden Road, Windsor - (Im not too sure if we should include our phone number or not ?? Please advise what you feel will look good etc

Happy for you to add a phrase or wording etc, as long as the specific details are included, above.

We also have an enclosed beer garden in the rear of the restaurant - Do you believe I should mention this?

I am really open to eye catching designs and ALL suggestions welcome please!
Updates

Please find attached of samples that I am sort of after: (please let me know if they cant be opened).

http://www.flyerquill.example/blog/wp-content/uploads/2012/06/happyHourPoster-e1340372894746.gif

http://marekvu.files.samplepress.example/2012/10/profolio_0012.jpg?w=1169

http://3.img.noteleaf.example/-NfNjpdG5w/T5pohPd0AhI/AAAAAAAADRs/CA7DPeI_PyU/s640/vintage_poster.jpg

http://www.orchidvane.example/files/imagecache/Event/news/teaser/Lounge_Happy_Hour_Poster_-_Mar_2011_bilingual.jpg

http://www.tkrumps.example/dallas/images/happyhour_poster.jpg

http://cdn2-b.newsgrove.example/sites/default/files/styles/large_lightbox/hash/9a/d1/9ad11350ba178511886fddcff7aaac8d.jpg?itok=wDl2vlfJ

http://www.platterpicks.example/imageservice/images/13/1313171414293_244/img_large_watermarked.jpg

Target Market(s)

18 YEARS OLD AND OVER

Industry/Entity Type

Restaurant

Requirements
Must have
• Address
Phone Number
Logo
Clear easy to read font, to be seen via cars + ppl walking down street
If images are included, to be clear and visable
Nice to have
• Images are possible
To mention a beer garden
Should not have
• Traditional Mexican Colourful 80's Theme

```html
<!DOCTYPE html>
<html lang="en">
<head>
<meta charset="utf-8">
<title>Happy Hour – Casa Lupita</title>
<link rel="stylesheet" href="https://fonts.googleapis.com/css2?family=Sancreek&family=Quicksand:wght@700&display=swap">
<style>
  :root {
    --ink: #0d0d0d;
    --paper: #fbf4f4;
    --frame: #9a9a9a;
    --wave-pink: #f4c9cf;
    --wave-blue: #cfe0ee;
    --wave-yellow: #f6e7bf;
    --wave-orange: #f3d3bd;
    --badge: #ffffff;
  }
  html, body {
    margin: 0;
    padding: 0;
    width: 852px;
    height: 1200px;
    overflow: hidden;
    background: var(--paper);
  }
  .poster {
    position: relative;
    width: 852px;
    height: 1200px;
    box-sizing: border-box;
    border: 2px solid var(--frame);
    overflow: hidden;
    color: var(--ink);
    font-family: "Sancreek", "Rye", serif;
  }
  .poster__pattern {
    position: absolute;
    inset: 0;
    background: linear-gradient(135deg, var(--wave-pink) 0%, var(--wave-blue) 28%, var(--wave-yellow) 52%, var(--wave-orange) 74%, var(--wave-pink) 100%);
    opacity: 0.85;
  }
  .poster__content {
    position: absolute;
    inset: 0;
    text-align: center;
  }
  .headline,
  .offer {
    position: absolute;
    left: 0;
    right: 0;
    margin: 0;
    font-weight: 400;
    line-height: 1;
    white-space: nowrap;
  }
  .headline {
    text-transform: uppercase;
    letter-spacing: 4px;
  }
  .headline--happy { top: 0; font-size: 236px; }
  .headline--hour  { top: 212px; font-size: 236px; }
  .offer { font-variant: small-caps; }
  .offer--drinks     { top: 488px; left: 40px; font-size: 62px; }
  .offer--margaritas { top: 578px; font-size: 88px; }
  .offer--days       { top: 698px; font-size: 58px; }
  .offer--time       { top: 772px; font-size: 112px; letter-spacing: 4px; }
  .ul {
    text-decoration: underline;
    text-decoration-thickness: 3px;
    text-underline-offset: 6px;
  }
  .ul--double {
    text-decoration-line: underline;
    text-decoration-style: double;
    text-decoration-thickness: 3px;
    text-underline-offset: 8px;
  }
  .ul--over {
    text-decoration-line: underline overline;
    text-decoration-thickness: 3px;
    text-underline-offset: 6px;
  }
  .address {
    position: absolute;
    left: 31px;
    top: 1078px;
    margin: 0;
    font-family: "Quicksand", "Arial Rounded MT Bold", sans-serif;
    font-weight: 700;
    font-size: 27px;
    letter-spacing: 1px;
    text-transform: uppercase;
    white-space: nowrap;
  }
  .brand {
    position: absolute;
    left: 596px;
    top: 1020px;
    width: 200px;
    height: 142px;
    background: var(--badge);
    display: flex;
    flex-direction: column;
    align-items: center;
    justify-content: center;
    gap: 10px;
  }
  .brand__dot {
    width: 18px;
    height: 18px;
    border-radius: 50%;
    background: var(--ink);
  }
  .brand__name {
    font-family: "Sancreek", "Rye", serif;
    font-size: 34px;
    line-height: 1;
    color: var(--ink);
    white-space: nowrap;
  }
</style>
</head>
<body>
  <main class="poster">
    <div class="poster__pattern" role="img" aria-label="Soft pastel zigzag wave pattern background"></div>
    <div class="poster__content">
      <h1 class="headline headline--happy">Happy</h1>
      <h1 class="headline headline--hour">Hour!</h1>
      <p class="offer offer--drinks">$4 <span class="ul">Beer</span>, <span class="ul">Wine</span> <span class="ul--double">and</span> Spirits</p>
      <p class="offer offer--margaritas">$5 M<span class="ul--double">argarita</span>s</p>
      <p class="offer offer--days"><span class="ul--over">everynight</span> <span class="ul--over">between</span></p>
      <p class="offer offer--time"><span class="ul--double">5:30 - 7:30</span></p>
      <p class="address">42 Lowden Road, Windsor</p>
      <div class="brand">
        <span class="brand__dot"></span>
        <span class="brand__name">Casa Lupita</span>
      </div>
    </div>
  </main>
</body>
</html>
```